Flyer design for corporate telephone business

We are a new company called "Harbourline Voice" that sells complete tailored phone solutions to businesses in Australia. In most cases we can also save many businesses 50%+ off their monthly telephone bill. They also get to keep their existing telephone numbers. We also provide complete new set-up of business phone equipment and services. So I would like these 3 points highlighted and to stand out. We utilise the latest technology with advanced features. The flyer should be A5 sized. Single sided. White background with mainly a lot of blue. Also a mixture of grey, a little bit of black etc. The final design should make the potential customer want to call us to find out more info.
Target Market(s)
Business Owners, Managers, Decision makers
Industry/Entity Type
Telecommunications
Requirements
Must have
- Flyer must highlight the 3 x call to actions. Below is order of priority
- 1. We help businesses save 50%+ on their monthly phone bill
- 2. Keep your existing telephone numbers
- 3. Brand new phone installation services or upgrades.
- Also contact details
- sales@harbourlinevoice.com.au
- ph: 58170926
Nice to have
- I would like to try and include as many product images attached to this brief as possible without making the flyer look to busy. I would like the customer to know that we can supply phones, video conferencing, headsets, etc Our logo is currently being designed on another project. This should be finished shortly and I can add this to the brief once I have the finished design.

```html
<!DOCTYPE html>
<html lang="en">
<head>
<meta charset="utf-8">
<title>Harbourline Voice – Flyer</title>
<link rel="stylesheet" href="https://fonts.googleapis.com/css2?family=Lato:wght@300;400&family=Roboto+Condensed:wght@400;700&display=swap">
<style>
  :root {
    --blue: #1f5fb0;
    --blue-dark: #164a8c;
    --blue-text: #2a6fc2;
    --ink: #1b1b1b;
    --charcoal: #2b2b2b;
    --grey-light: #eeeeee;
    --grey-mid: #d4d4d4;
    --grey-text: #555555;
    --white: #ffffff;
  }
  * { margin: 0; padding: 0; box-sizing: border-box; }
  html, body { width: 853px; height: 1200px; overflow: hidden; background: var(--white); }
  .flyer {
    position: relative;
    width: 853px; height: 1200px;
    background: var(--white);
    font-family: "Lato", sans-serif;
    overflow: hidden;
  }
  .header {
    position: absolute; left: 0; top: 0; width: 853px; height: 440px;
    background: linear-gradient(90deg, #ffffff 0%, #f7f7f7 100%);
  }
  .header-photo {
    position: absolute; right: 0; top: 0; width: 470px; height: 440px;
    background: linear-gradient(90deg, rgba(240,240,240,0) 0%, #dcdfe3 30%, #c9ced5 70%, #b9bfc8 100%);
  }
  .brand-name {
    position: absolute; left: 40px; top: 70px;
    font-weight: 300; font-size: 54px; color: var(--charcoal); letter-spacing: -0.5px;
  }
  .brand-tagline {
    position: absolute; left: 42px; top: 134px;
    font-weight: 400; font-size: 23px; color: var(--grey-text);
  }
  .intro-band {
    position: absolute; left: 0; top: 440px; width: 853px; height: 100px;
    background: var(--charcoal);
    color: #d8d8d8; font-size: 15px; line-height: 22px; text-align: center;
    padding: 22px 60px 0;
  }
  .benefits {
    position: absolute; left: 0; top: 540px; width: 853px; height: 570px;
    background: linear-gradient(180deg, #fafafa 0%, var(--grey-light) 55%, var(--grey-mid) 100%);
  }
  .benefit { position: absolute; left: 0; width: 853px; height: 100px; }
  .benefit-number {
    position: absolute; left: 28px; top: -8px;
    font-family: "Roboto Condensed", sans-serif; font-weight: 700;
    font-size: 112px; line-height: 112px; color: var(--ink);
  }
  .benefit-bar {
    position: absolute; left: 92px; right: 0; top: 22px; height: 64px;
    background: linear-gradient(180deg, var(--blue) 0%, var(--blue-dark) 100%);
    color: var(--white);
    font-family: "Roboto Condensed", sans-serif; font-size: 29px;
    line-height: 64px; padding-left: 28px;
  }
  .products {
    position: absolute; left: 50px; top: 930px; width: 400px; height: 140px;
  }
  .product { position: absolute; bottom: 0; border-radius: 8px; }
  .product-a { left: 0; width: 150px; height: 110px; background: linear-gradient(180deg, #5a5f66, #25282c); }
  .product-b { left: 160px; width: 70px; height: 140px; background: linear-gradient(180deg, #4a4f55, #1d1f22); }
  .product-c { left: 240px; width: 160px; height: 115px; background: linear-gradient(180deg, #5a5f66, #25282c); }
  .call-us {
    position: absolute; right: 40px; top: 945px; width: 330px;
    font-family: "Roboto Condensed", sans-serif;
  }
  .call-label { font-size: 42px; color: var(--charcoal); line-height: 46px; letter-spacing: 0.5px; }
  .call-number { font-size: 46px; color: var(--blue-text); line-height: 56px; }
  .footer-band {
    position: absolute; left: 0; top: 1110px; width: 853px; height: 56px;
    background: var(--charcoal);
    color: #cfcfcf; font-size: 17px; letter-spacing: 1px;
    line-height: 56px; padding-left: 40px;
  }
  .footer-band .divider { color: var(--white); margin: 0 14px; }
</style>
</head>
<body>
<div class="flyer">
  <section class="header">
    <div class="header-photo" role="img" aria-label="Photo of a smiling office worker on a desk phone in front of a computer monitor"></div>
    <h1 class="brand-name">Harbourline Voice</h1>
    <p class="brand-tagline">Phone systems for your business</p>
  </section>

  <p class="intro-band">We really love working for you and your customers.<br>We are Tidewater Group and we do awesome themes. We do what we love and this is the best in our life. Try a piece of our work and you will not want to swap for anything else!</p>

  <section class="benefits">
    <div class="benefit" style="top:30px">
      <span class="benefit-number">1</span>
      <div class="benefit-bar">We help businesses save 50%+ on their monthly phone bill</div>
    </div>
    <div class="benefit" style="top:145px">
      <span class="benefit-number">2</span>
      <div class="benefit-bar">Keep your existing telephone numbers</div>
    </div>
    <div class="benefit" style="top:260px">
      <span class="benefit-number">3</span>
      <div class="benefit-bar">Brand new phone installation services or upgrades.</div>
    </div>
  </section>

  <div class="products">
    <div class="product product-a" role="img" aria-label="Business desk phone with display"></div>
    <div class="product product-b" role="img" aria-label="Cordless handset in charging cradle"></div>
    <div class="product product-c" role="img" aria-label="Colour screen IP desk phone"></div>
  </div>

  <div class="call-us">
    <p class="call-label">CALL US TODAY</p>
    <p class="call-number">(08) 5817-0926</p>
  </div>

  <footer class="footer-band">sales@harbourlinevoice.com.au<span class="divider">|</span>www.harbourlinevoice.com.au</footer>
</div>
</body>
</html>
```